The book is for children, and is an exciting short story. It centres around the The Phantom of Carrowfell Heath.

In British folklore, The Phantom of Carrowfell Heath is a phantom wild cat thought to live in Cornwall, England, United Kingdom. Bodmin Moor became a centre of purported sightings after 1978, with occasional reports of mutilated slain livestock; the alleged panther/ leopard-like black cats of the same region came to be popularly known as The Phantom of Carrowfell Heath.

The book is for students aged 11 to 15 years, (catch-up reading). It's also for students of English as a foreign language.

Text required on Front Cover:

The Phantom of Carrowfell Heath

Harold Quint

```html
<!DOCTYPE html>
<html lang="en">
<head>
<meta charset="utf-8">
<title>The Phantom of Carrowfell Heath – Cover</title>
<link href="https://fonts.googleapis.com/css2?family=Teko:wght@500;600&family=Kurale&display=swap" rel="stylesheet">
<style>
  :root {
    --page-bg: #ececec;
    --cover-navy: #0f1322;
    --title-orange: #f08a1c;
    --title-gold: #f7c531;
    --block-yellow: #f6b625;
    --text-light: #e9e9ee;
    --rule: #c9cad3;
    --scene-glow: #7fa6e0;
    --scene-blue: #2b3b8c;
    --scene-deep: #141a3d;
  }
  * { box-sizing: border-box; margin: 0; padding: 0; }
  html, body { width: 796px; height: 1200px; overflow: hidden; background: var(--page-bg); }
  .cover-spread {
    position: absolute; left: 0; top: 302px;
    width: 796px; height: 596px;
    background: var(--cover-navy);
    font-family: "Kurale", serif;
    color: var(--text-light);
  }
  .title {
    font-family: "Teko", sans-serif;
    font-weight: 600;
    text-transform: uppercase;
    line-height: 0.9;
    background: linear-gradient(180deg, var(--title-orange), var(--title-gold));
    -webkit-background-clip: text; background-clip: text;
    color: transparent;
  }
  .title .small-of {
    font-family: "Kurale", serif; text-transform: none; font-weight: 400;
    font-size: 0.5em;
  }

  /* Back panel */
  .back-panel { position: absolute; left: 0; top: 0; width: 376px; height: 596px; }
  .back-title { position: absolute; left: 0; width: 376px; top: 26px; text-align: center; font-size: 40px; }
  .back-rule {
    position: absolute; left: 66px; top: 116px; width: 250px; height: 1px;
    background: linear-gradient(90deg, transparent, var(--rule), transparent);
  }
  .blurb {
    position: absolute; left: 29px; top: 128px; width: 334px;
    font-size: 9.6px; line-height: 14.2px; text-align: justify;
  }
  .author-heading {
    position: absolute; left: 111px; top: 258px;
    font-size: 15px; letter-spacing: 3px;
  }
  .author-bio {
    position: absolute; left: 29px; top: 283px; width: 334px;
    font-size: 9.6px; line-height: 14.2px; text-align: justify;
  }
  .author-photo {
    float: left; width: 74px; height: 94px; margin: 1px 8px 2px 0;
    background: var(--block-yellow);
  }
  .back-block {
    position: absolute; left: 206px; top: 483px; width: 135px; height: 75px;
    background: var(--block-yellow);
  }

  /* Spine */
  .spine { position: absolute; left: 376px; top: 0; width: 36px; height: 596px; }
  .spine-title {
    position: absolute; left: 8px; top: 113px;
    writing-mode: vertical-rl; font-size: 15px; white-space: nowrap;
  }
  .spine-author {
    position: absolute; left: 9px; top: 385px;
    writing-mode: vertical-rl; font-size: 15px; white-space: nowrap;
  }

  /* Front panel */
  .front-panel { position: absolute; left: 412px; top: 0; width: 384px; height: 596px; overflow: hidden; }
  .cover-art {
    position: absolute; inset: 0;
    background:
      radial-gradient(ellipse 45% 40% at 50% 40%, var(--scene-glow), transparent 75%),
      linear-gradient(180deg, var(--cover-navy) 0%, var(--scene-deep) 12%, var(--scene-blue) 45%, var(--scene-deep) 80%, var(--cover-navy) 100%);
  }
  .front-title {
    position: absolute; left: 0; width: 384px; top: 22px; text-align: center;
    font-size: 46px;
  }
  .front-author {
    position: absolute; left: 0; width: 384px; top: 534px; text-align: center;
    font-size: 31px; color: #ffffff;
  }
</style>
</head>
<body>
  <main class="cover-spread">
    <section class="back-panel">
      <h2 class="title back-title">The Phantom <span class="small-of">of</span><br>Carrowfell Heath</h2>
      <div class="back-rule"></div>
      <p class="blurb">There are many variations of passages of Lorem Ipsum available, but the majority have suffered alteration in some form, by injected able. If you are going to use a passage of Lorem Ipsum, you need to be sure there isn't anything embarrassing hidden in the middle of text. All the Lorem Ipsum generators on the Internet tend to repeat predefined chunks as necessary, making this the first true generator on the Internet. It uses a dictionary of over 200 Latin words, combined with a handful of model sentence structures.</p>
      <h3 class="author-heading">Harold Quint</h3>
      <p class="author-bio"><span class="author-photo" role="img" aria-label="Author photograph"></span>Lorem Ipsum is simply dummy text of the printing and typesetting industry. Lorem Ipsum has been the industry's standard dummy text ever since the 1500s, when an unknown printer took a galley of type and scrambled it to make a type specimen book. It has survived not only five centuries, but also the leap into electronic typesetting, remaining essentially unchanged. It was popularised in the 1960s with the release of Typecraft sheets containing Lorem Ipsum passages, and more recently with desktop publishing software like Pagewright Studio including versions of Lorem Ipsum.</p>
      <div class="back-block"></div>
    </section>

    <section class="spine">
      <p class="title spine-title">The Phantom <span class="small-of">of</span> Carrowfell Heath</p>
      <p class="spine-author">Harold Quint</p>
    </section>

    <section class="front-panel">
      <div class="cover-art" role="img" aria-label="Illustration of a black cat with yellow eyes sitting on moonlit rocks in a misty blue forest with bats"></div>
      <h1 class="title front-title">The Phantom <span class="small-of">of</span><br>Carrowfell Heath</h1>
      <p class="front-author">Harold Quint</p>
    </section>
  </main>
</body>
</html>
```